Napa Winery - Chardonnay wine label

We are looking for a label for a new Napa Valley winery - chardonnay wine. The winery is "Marrowbrook Hill Vintners" and we would like to see it depicted on a white wine (chardonnay style) bottle. The winery is called Marrowbrook Hill Vintners.

We are open to ideas!

Target Market(s)

High-end chardonnay lovers

Requirements
Nice to have
• Painted or etched label onto bottle

```html
<!DOCTYPE html>
<html lang="en">
<head>
<meta charset="utf-8">
<title>Marrowbrook Hill Vintners – Chardonnay Label</title>
<link rel="stylesheet" href="https://fonts.googleapis.com/css2?family=Jost:wght@400&display=swap">
<style>
  :root {
    --backdrop: #d9d7dc;
    --label-paper: #ffffff;
    --ink: #0c0c0c;
    --pattern-light: #ececec;
    --pattern-mid: #8a8a8a;
    --pattern-dark: #101010;
    --tag-text: #ffffff;
  }
  * { box-sizing: border-box; margin: 0; padding: 0; }
  html, body {
    width: 1200px;
    height: 1172px;
    overflow: hidden;
    background: var(--backdrop);
  }
  .canvas {
    position: relative;
    width: 1200px;
    height: 1172px;
  }
  .wine-label {
    position: absolute;
    left: 210px;
    top: 66px;
    width: 780px;
    height: 1040px;
    background: var(--label-paper);
  }
  .chevron-field {
    position: absolute;
    left: 62px;
    top: 58px;
    width: 656px;
    height: 900px;
    background: linear-gradient(to bottom,
      var(--pattern-light) 0%,
      var(--pattern-mid) 45%,
      var(--pattern-dark) 100%);
  }
  .brand-tag {
    position: absolute;
    left: 62px;
    top: 396px;
    width: 430px;
    height: 150px;
    background: var(--ink);
    display: flex;
    flex-direction: column;
    justify-content: center;
    padding: 0 30px;
  }
  .brand-name {
    font-family: "Jost", "Futura", sans-serif;
    font-weight: 400;
    color: var(--tag-text);
    font-size: 38px;
    line-height: 1.2;
    letter-spacing: 0.02em;
    text-transform: uppercase;
  }
</style>
</head>
<body>
  <main class="canvas">
    <section class="wine-label">
      <div class="chevron-field" role="img" aria-label="Zigzag chevron line pattern growing denser from light at the top to black at the bottom"></div>
      <div class="brand-tag">
        <p class="brand-name">Marrowbrook Hill<br>Vintners</p>
      </div>
    </section>
  </main>
</body>
</html>
```